eJuice bottle label

We need a design for a label we are putting on eJuice liquid glass bottles, I have attached what we have in mind. We are a Colorado family ran business so we are going to name our flavors after Colorado Passes and would like a picture of the pass on the bottle. There will be 5 total labels.

```html
<!DOCTYPE html>
<html lang="en">
<head>
<meta charset="utf-8">
<title>Elk Ridge – Raven Rock Pass Label</title>
<link rel="stylesheet" href="https://fonts.googleapis.com/css2?family=Tinos&family=Arimo:wght@400;700&display=swap">
<style>
  :root {
    --red-deep: #7a1a0e;
    --red-mid: #b23a1c;
    --red-warm: #c9502a;
    --ink-white: #ffffff;
    --ink-soft: #f1e3dc;
    --sky: #cfd8e2;
    --rock: #a48a80;
    --silver-light: #f4f4f4;
    --silver-dark: #9a9a9a;
    --tail: #4a4a4a;
    --outline: #1c1c1c;
  }
  html, body {
    margin: 0;
    padding: 0;
    overflow: hidden;
    background: #ffffff;
  }
  .label {
    position: relative;
    width: 1200px;
    height: 510px;
    overflow: hidden;
    background:
      radial-gradient(ellipse at 55% 45%, var(--red-warm) 0%, var(--red-mid) 45%, var(--red-deep) 100%);
  }
  .label-art {
    position: absolute;
    inset: 0;
  }
  .brand-title {
    font-family: "Tinos", serif;
    font-size: 54px;
    letter-spacing: 4px;
    fill: var(--ink-white);
  }
  .strength {
    font-family: "Tinos", serif;
    fill: var(--ink-white);
  }
  .flavor-name {
    font-family: "Tinos", serif;
    font-size: 38px;
    fill: #111111;
  }
  .origin-line {
    font-family: "Tinos", serif;
    font-size: 30px;
    letter-spacing: 1px;
    fill: var(--ink-white);
  }
  .side-copy {
    position: absolute;
    top: 496px;
    width: 470px;
    transform: rotate(-90deg);
    transform-origin: top left;
    font-family: "Arimo", sans-serif;
    color: var(--ink-soft);
    margin: 0;
  }
  .warning { left: 8px; font-size: 22px; line-height: 25px; }
  .warning strong { display: block; color: var(--ink-white); font-size: 24px; line-height: 28px; }
  .ingredients { left: 1070px; font-size: 22px; line-height: 25px; }
</style>
</head>
<body>
<div class="label">
  <svg class="label-art" width="1200" height="510" viewBox="0 0 1200 510">
    <defs>
      <linearGradient id="scene-tone" x1="0" y1="0" x2="0" y2="1">
        <stop offset="0" stop-color="var(--sky)"/>
        <stop offset="0.45" stop-color="#c4b3ac"/>
        <stop offset="1" stop-color="var(--rock)"/>
      </linearGradient>
      <linearGradient id="silver" x1="0" y1="0" x2="0" y2="1">
        <stop offset="0" stop-color="var(--silver-dark)"/>
        <stop offset="0.35" stop-color="var(--silver-light)"/>
        <stop offset="0.7" stop-color="#e2e2e2"/>
        <stop offset="1" stop-color="var(--silver-dark)"/>
      </linearGradient>
    </defs>

    <text class="brand-title" x="612" y="68" text-anchor="middle">ELK RIDGE</text>

    <text class="strength" x="884" y="63" font-size="46">3<tspan font-size="36">MG</tspan></text>

    <g class="pass-scene">
      <ellipse cx="605" cy="255" rx="249" ry="183" fill="#ffffff" opacity="0.55"/>
      <ellipse class="pass-photo" role="img" aria-label="Photo of a mountain goat in front of a rock pinnacle at the pass"
        cx="605" cy="255" rx="244" ry="178" fill="url(#scene-tone)" stroke="var(--outline)" stroke-width="2"/>
    </g>

    <g class="flavor-banner">
      <polygon points="232,408 142,408 168,434 142,460 232,460" fill="var(--tail)" stroke="var(--outline)" stroke-width="2"/>
      <polygon points="968,408 1060,408 1034,434 1060,460 968,460" fill="var(--tail)" stroke="var(--outline)" stroke-width="2"/>
      <rect x="222" y="398" width="756" height="62" fill="url(#silver)" stroke="var(--outline)" stroke-width="2"/>
      <rect x="232" y="404" width="736" height="50" fill="none" stroke="#666666" stroke-width="1"/>
      <text class="flavor-name" x="600" y="442" text-anchor="middle">Raven Rock Pass Premium Elixer</text>
    </g>

    <text class="origin-line" x="600" y="492" text-anchor="middle">HAND CRAFTED IN COLORADO</text>
  </svg>

  <p class="side-copy warning"><strong>MUST BE 18 YEARS OF AGE</strong>TO PURCHASE. PRODUCT MAY<br>CONTAIN NICOTINE. KEEP AWAY<br>FROM CHILDREN &amp; PETS.</p>

  <p class="side-copy ingredients">Ingredient: &nbsp;USP Vegetable Glycer-<br>in, USP Propylene Glycol, natural/<br>artificial flavorings. May contain<br>Vaping Grade USP Nicotine.</p>
</div>
</body>
</html>
```